PowerPoint Template Needed for Investment Firm

Norvelle Capital Management is an emerging wealth management firm based in New Jersey. It offers superior investment returns to high net worth individuals and institutions by finding undervalued assets.

We recently selected a company logo which was inspired by the Tucana constellation. Beta Tucanae is a group of six stars, containing star cluster 47 Tucanae, rated the second brightest object in the sky.

Now we need a PowerPoint template with the designs for the following:

1. Title/cover page slide
2. Content slide with title
3. Section slide - to introduce a new section
4. Final slide - with contact information

The slides will be used at investor presentations, that is, to provide information about the company to potential investors. Since we are an investment firm, the design should project a sense of stability, growth and professionalism. The owner is interested in something simple yet striking, which of course is consistent with the logo. I'm thinking more conservative colors and Sans Serif fonts.

I plan on changing the status to non-refundable once I see some designs that I really like.

Target Market(s)

Wealthy individuals, probably middle aged or older, in the US

Industry/Entity Type

Conservative

Requirements
Must have
• Sans serif fonts
Clean, very professional look
Conservative colors that complement existing logo
Should not have
• Anything too busy or complicated

```html
<!DOCTYPE html>
<html lang="en">
<head>
<meta charset="utf-8">
<title>Norvelle Capital Management – Slide Template</title>
<link rel="stylesheet" href="https://fonts.googleapis.com/css2?family=Arimo:wght@400;600;700&display=swap">
<style>
  :root {
    --navy: #03205e;
    --slate: #333d4f;
    --grey: #a6a6a6;
    --charcoal: #3c3c3c;
    --gold: #fdd96a;
    --number-gold: #e2ad12;
    --mark-blue: #1d3a9c;
    --ink: #2f3b46;
    --white: #ffffff;
    --dash: #8a9bb5;
  }
  * { box-sizing: border-box; margin: 0; padding: 0; }
  html, body { width: 1200px; height: 848px; overflow: hidden; background: var(--white); }
  body { font-family: "Arimo", Arial, sans-serif; }
  .canvas { position: relative; width: 1200px; height: 848px; overflow: hidden; }
  .block { position: absolute; }

  .brand-square { position: absolute; background: var(--mark-blue); border-radius: 9px; }
  .brand-name { position: absolute; color: var(--ink); font-weight: 600; text-align: center; line-height: 1; }
  .brand-name .primary { display: block; letter-spacing: 4px; }
  .brand-name .secondary { display: block; }
  .mark-label { position: absolute; color: var(--white); font-weight: 600; font-size: 11px; text-align: center; width: 100%; top: 50%; transform: translateY(-50%); }

  /* Cover slide */
  .cover-band { left: 149px; top: 0; width: 301px; height: 132px; background: var(--grey); }
  .cover-base { left: 149px; top: 219px; width: 301px; height: 196px; background: var(--navy); }

  /* Agenda slide */
  .agenda-panel { left: 601px; top: 0; width: 337px; height: 415px; background: var(--slate); }
  .agenda-accent { left: 981px; top: 0; width: 219px; height: 107px; background: var(--gold); }
  .agenda-column { left: 981px; top: 107px; width: 219px; height: 308px; background: var(--navy); }
  .agenda-item { position: absolute; right: 269px; color: var(--white); font-size: 25px; line-height: 1; white-space: nowrap; }
  .agenda-item strong { font-weight: 700; }
  .agenda-number { position: absolute; left: 948px; width: 27px; height: 27px; border: 2px dashed var(--dash); border-radius: 4px; color: var(--number-gold); font-size: 19px; display: flex; align-items: center; justify-content: center; }

  /* Section slide */
  .section-header { left: 0; top: 435px; width: 505px; height: 97px; background: var(--slate); }
  .section-title { position: absolute; right: 725px; top: 492px; color: var(--white); font-size: 25px; white-space: nowrap; }
  .section-title strong { font-weight: 700; }
  .section-rail { left: 505px; top: 532px; width: 95px; height: 316px; background: var(--navy); }
  .rail-box { position: absolute; width: 36px; height: 37px; border: 2px dashed #5d7092; border-radius: 4px; color: var(--number-gold); font-size: 22px; display: flex; align-items: center; justify-content: center; }
  .section-notes { position: absolute; right: 728px; top: 559px; width: 380px; text-align: right; font-size: 12.5px; line-height: 1.33; color: #111; }
  .section-notes h3 { font-size: 12.5px; font-weight: 700; }
  .section-notes p { margin-bottom: 15px; }

  /* Closing slide */
  .closing-dark { left: 602px; top: 435px; width: 163px; height: 73px; background: var(--charcoal); }
  .closing-band { left: 765px; top: 435px; width: 435px; height: 73px; background: var(--grey); }
  .closing-panel { left: 765px; top: 660px; width: 435px; height: 188px; background: var(--navy); }
  .contact-line { position: absolute; left: 770px; color: var(--white); font-size: 13px; white-space: nowrap; }
</style>
</head>
<body>
<main class="canvas">

  <!-- Cover slide -->
  <section class="slide-cover">
    <div class="block cover-band"></div>
    <div class="brand-square" style="left:261px; top:32px; width:78px; height:80px;"></div>
    <div class="brand-name" style="left:149px; top:146px; width:301px;">
      <span class="primary" style="font-size:40px;">NORVELLE</span>
      <span class="secondary" style="font-size:23px; margin-top:4px;">Capital Management</span>
    </div>
    <div class="block cover-base"></div>
  </section>

  <!-- Agenda slide -->
  <section class="slide-agenda">
    <div class="block agenda-panel"></div>
    <div class="block agenda-accent"></div>
    <div class="block agenda-column"></div>
    <div class="brand-square" style="left:1116px; top:9px; width:78px; height:79px;"><span class="mark-label">Norvelle</span></div>

    <div class="agenda-item" style="top:153px;"><strong>Legal</strong> Disclaimers</div>
    <div class="agenda-item" style="top:193px;"><strong>Investment</strong> Strategy</div>
    <div class="agenda-item" style="top:229px;"><strong>Financial</strong> Returns</div>
    <div class="agenda-item" style="top:267px;"><strong>Manager</strong> Biography</div>

    <div class="agenda-number" style="top:154px;">1</div>
    <div class="agenda-number" style="top:193px;">2</div>
    <div class="agenda-number" style="top:229px;">3</div>
    <div class="agenda-number" style="top:266px;">4</div>
  </section>

  <!-- Section slide -->
  <section class="slide-section">
    <div class="block section-header"></div>
    <h2 class="section-title"><strong>Investment</strong> Strategy</h2>
    <div class="brand-square" style="left:512px; top:443px; width:80px; height:80px;"><span class="mark-label">Norvelle</span></div>
    <div class="block section-rail"></div>
    <div class="rail-box" style="left:511px; top:538px;"></div>
    <div class="rail-box" style="left:553px; top:538px;">2</div>
    <div class="rail-box" style="left:511px; top:579px;"></div>
    <div class="rail-box" style="left:553px; top:579px;"></div>

    <div class="section-notes">
      <h3>General comments:</h3>
      <p>This design: is under consideration. Please make some changes.</p>
      <p>I like the look of all the slides especially this page for the section headers/titles. One thing I would like changed on this slide is the way the corporate logo appears. It gets lost on the blue background. Could you try to showcase the logo in a different way? Also, this is minor but the numbers don't seem to be centered in those blue boxes.</p>
      <p>Thanks.</p>
    </div>
  </section>

  <!-- Closing slide -->
  <section class="slide-closing">
    <div class="block closing-dark"></div>
    <div class="block closing-band"></div>
    <div class="brand-square" style="left:770px; top:527px; width:80px; height:81px;"></div>
    <div class="brand-name" style="left:768px; top:614px; width:140px;">
      <span class="primary" style="font-size:19px; letter-spacing:2px;">NORVELLE</span>
      <span class="secondary" style="font-size:11.5px; margin-top:2px;">Capital Management</span>
    </div>
    <div class="block closing-panel"></div>
    <div class="contact-line" style="top:668px;">48 Harbor Ave. Newark, NJ 07102</div>
    <div class="contact-line" style="top:690px; left:773px;">jdalton@norvellecap.com</div>
    <div class="contact-line" style="top:706px; left:773px;">www.norvellecap.com</div>
  </section>

</main>
</body>
</html>
```